I am a Financial Adviser specialising in Aged Care Advice. We provide financial advice and assistance to families with loved ones entering an Aged Care facility.
We need a flyer detailing the Aged Care Packages that we offer. There will be 3 main packages & then other add ons. I need an area where the client can sign off on the package/s that they choose. I have attached a sample to demonstrate the required layout, and a copy of content. I would like the flyer to have an image as per the attached sample, and to be designed in soft pastels, blues, greens.

Financial

```html
<!DOCTYPE html>
<html lang="en">
<head>
<meta charset="utf-8">
<title>Aged Care Services Flyer</title>
<link href="https://fonts.googleapis.com/css2?family=Cinzel:wght@700&family=Oswald:wght@600&family=Lato:ital,wght@0,400;0,700;1,400&family=Gochi+Hand&display=swap" rel="stylesheet">
<style>
  :root {
    --gold: #d4a514;
    --gold-light: #f0c42a;
    --charcoal: #3b3b3b;
    --ink: #1f1f1f;
    --white: #ffffff;
    --text-dark: #2a2a2a;
  }
  html, body { margin: 0; padding: 0; }
  body { width: 902px; height: 1200px; overflow: hidden; background: var(--white); }
  .flyer { position: relative; width: 902px; height: 1200px; overflow: hidden; background: var(--white); font-family: 'Lato', sans-serif; }

  .brand { position: absolute; left: 52px; top: 44px; display: flex; align-items: center; gap: 8px; }
  .brand-dot { width: 14px; height: 14px; border-radius: 50%; background: var(--gold); }
  .brand-name { font-family: 'Lato', sans-serif; font-weight: 700; font-size: 19px; color: var(--ink); letter-spacing: 0.5px; }

  .title { position: absolute; left: 286px; top: 30px; margin: 0; font-family: 'Cinzel', serif; font-weight: 700; font-size: 47px; color: var(--ink); letter-spacing: 0.5px; white-space: nowrap; }
  .title .accent { color: var(--gold); }

  .hero { position: absolute; left: 0; top: 100px; }
  .lower-panel { position: absolute; left: 0; top: 440px; width: 902px; height: 727px; background: var(--charcoal); }
  .star { position: absolute; left: 703px; top: 336px; }

  .package-head { position: absolute; left: 34px; display: flex; align-items: center; white-space: nowrap; }
  .checkbox { width: 28px; height: 28px; background: var(--white); border: 2px solid #cfcfcf; box-sizing: border-box; margin-right: 12px; }
  .package-name { font-family: 'Oswald', sans-serif; font-weight: 600; font-size: 27px; color: var(--gold-light); text-transform: uppercase; letter-spacing: 0.3px; }
  .package-tagline { font-family: 'Lato', sans-serif; font-style: italic; font-size: 20px; color: var(--white); margin-left: 2px; }

  .package-box { position: absolute; left: 34px; width: 844px; background: var(--white); border: 3px solid var(--gold); border-radius: 18px; box-sizing: border-box; }
  .item { position: absolute; font-style: italic; font-size: 13.5px; color: var(--text-dark); white-space: nowrap; padding-left: 20px; }
  .item::before { content: ""; position: absolute; left: 0; top: 50%; width: 9px; height: 9px; margin-top: -5px; border-radius: 50%; background: var(--gold); }
  .mood { position: absolute; font-family: 'Gochi Hand', cursive; font-size: 17px; color: var(--gold); white-space: nowrap; }
  .includes { position: absolute; left: 56px; font-size: 13.5px; color: var(--ink); text-transform: uppercase; white-space: nowrap; }
  .includes span { color: var(--gold); text-transform: none; }
  .disclaimer { position: absolute; left: 74px; top: 98px; font-style: italic; font-size: 11.5px; color: var(--text-dark); white-space: nowrap; letter-spacing: 0.1px; }

  .footer-line { position: absolute; left: 0; top: 1166px; width: 902px; height: 5px; background: var(--white); }
  .footer-band { position: absolute; left: 0; top: 1171px; width: 902px; height: 29px; background: var(--gold); }
</style>
</head>
<body>
<div class="flyer">

  <div class="brand"><span class="brand-dot"></span><span class="brand-name">Brightway Finance</span></div>
  <h1 class="title">AGED CARE <span class="accent">SERVICES</span></h1>

  <div class="lower-panel"></div>

  <svg class="hero" width="902" height="400" viewBox="0 0 902 400">
    <defs>
      <linearGradient id="meadow" x1="0" y1="0" x2="0" y2="1">
        <stop offset="0" stop-color="#b7c58a"/>
        <stop offset="0.45" stop-color="#d9cfc0"/>
        <stop offset="1" stop-color="#8fa85a"/>
      </linearGradient>
    </defs>
    <path d="M0,45 Q420,-25 902,70 L902,300 Q451,470 0,330 Z" fill="var(--gold)"/>
    <path d="M0,330 Q451,470 902,300" fill="none" stroke="var(--white)" stroke-width="4"/>
    <g role="img" aria-label="Photo of a smiling multi-generation family sitting together on the grass outdoors">
      <path d="M0,110 Q420,20 902,150 L902,300 Q451,420 0,290 Z" fill="url(#meadow)"/>
    </g>
    <path d="M0,110 Q420,20 902,150" fill="none" stroke="var(--ink)" stroke-width="2"/>
  </svg>

  <svg class="star" width="200" height="200" viewBox="-100 -100 200 200">
    <polygon points="0,-90 21.2,-29.1 85.6,-27.8 34.2,11.1 52.9,72.8 0,36 -52.9,72.8 -34.2,11.1 -85.6,-27.8 -21.2,-29.1" fill="var(--gold)" stroke="var(--white)" stroke-width="5" stroke-linejoin="round"/>
  </svg>

  <!-- Essentials -->
  <div class="package-head" style="top:558px;">
    <span class="checkbox"></span>
    <span class="package-name">Essentials Package $770.......</span>
    <span class="package-tagline">When you know what you want....</span>
  </div>
  <div class="package-box" style="top:608px; height:126px;">
    <span class="item" style="left:49px; top:14px;">Explanation of Aged Care Fees and Charges.</span>
    <span class="mood" style="left:354px; top:10px;">Peace of Mind</span>
    <span class="item" style="left:49px; top:39px;">Preliminary Home/Assets Assessment.*</span>
    <span class="item" style="left:49px; top:64px;">Estimated Means Tested Fee Calculation.*</span>
    <span class="item" style="left:501px; top:14px;">Preliminary Aged Care Costs.*</span>
    <span class="item" style="left:501px; top:39px;">Estimated Cash Flow Scenario.*</span>
    <span class="disclaimer">*PLEASE NOTE THIS IS GENERAL FACTUAL INFORMATION ONLY.&nbsp; WE DO NOT PROVIDE ANY SPECIFIC PERSONAL INFORMATION.</span>
  </div>

  <!-- Advantage -->
  <div class="package-head" style="top:765px;">
    <span class="checkbox"></span>
    <span class="package-name">Advantage Package $2,970....</span>
    <span class="package-tagline">When you need to know all the options....</span>
  </div>
  <div class="package-box" style="top:819px; height:129px;">
    <span class="includes" style="top:12px;">Essentials <span>Package plus</span></span>
    <span class="item" style="left:49px; top:38px;">Analyse and Strategize Aged Care costs.</span>
    <span class="mood" style="left:330px; top:34px;">Confidence</span>
    <span class="item" style="left:49px; top:63px;">Compare up to 5 Strategy options.</span>
    <span class="item" style="left:49px; top:88px;">Minimise Aged Care Costs (where possible).</span>
    <span class="item" style="left:501px; top:32px;">Maximise Age Pension Income (where possible).</span>
    <span class="item" style="left:501px; top:57px;">Prepare a Full Statement of Advice (SOA).</span>
    <span class="item" style="left:501px; top:82px;">Implementation of Aged Care Strategy.</span>
  </div>

  <!-- Platinum -->
  <div class="package-head" style="top:979px;">
    <span class="checkbox"></span>
    <span class="package-name">Boxplatinum Package $5,940....</span>
    <span class="package-tagline">When you need someone to take charge...</span>
  </div>
  <div class="package-box" style="top:1026px; height:128px;">
    <span class="includes" style="top:12px;">Advantage <span>Package plus</span></span>
    <span class="item" style="left:49px; top:40px;">Liase with the Aged Care Facility.</span>
    <span class="mood" style="left:286px; top:36px;">Convenience</span>
    <span class="item" style="left:49px; top:65px;">CentreLink/DVA Nominee.</span>
    <span class="item" style="left:49px; top:90px;">Post Entry Review.</span>
    <span class="item" style="left:501px; top:30px;">Post Implementation SOA (if required).</span>
    <span class="item" style="left:501px; top:55px;">Annual Review.</span>
  </div>

  <div class="footer-line"></div>
  <div class="footer-band"></div>
</div>
</body>
</html>
```